Fashion Boutique shop and Fashion designer needs a business card (two in one)

This is a new business, I like light colors but very colorful. I would love attractive, one of a kind design :-)
On the back side I would like a white unicorn with rainbow color hair. On the back of the card around or under, not covering the unicorn I would like a quotation "Sometimes the smallest things take up the most room in your heart" Bramble the Mole - or any lovely quote about love and gratitude.
Thank you very much.

Target Market(s)

Age 16-100 who loves unique clothing and shoes and lots of colours.

Industry/Entity Type

Business

Contact Information for Business Card

The boutique's name is Lark's Design
Mira
021 587 3904
Boutique owner - Fashion designer
The Arbour - Christchurch

Font styles to use
Script

Requirements
Must have
• some lovely dress or dresses, shoes, a woman with a nice colorful dress on, high heels or a dress as its getting made :-)

```html
<!DOCTYPE html>
<html lang="en">
<head>
<meta charset="utf-8">
<title>Lark's Design – Business Card</title>
<link rel="stylesheet" href="https://fonts.googleapis.com/css2?family=Dancing+Script:wght@700&family=Questrial&display=swap">
<style>
  :root {
    --page: #eeeeee;
    --card: #ffffff;
    --frame: #c9c9c9;
    --ink-grey: #9a9a9a;
    --ink-dark: #7d7d7d;
    --brand: #d98bb4;
    --yellow: #e8c92a;
    --orange: #f0a23a;
    --pink: #ec7fa8;
    --purple: #a57bc4;
    --blue: #4fb3e0;
    --green: #86c24a;
    --silhouette: #d2d2d2;
  }
  * { box-sizing: border-box; margin: 0; padding: 0; }
  html, body { width: 1200px; height: 1000px; overflow: hidden; }
  body {
    background: var(--page);
    font-family: "Questrial", sans-serif;
    display: flex;
    flex-direction: column;
    align-items: center;
    justify-content: center;
    gap: 40px;
  }
  .card {
    position: relative;
    width: 760px;
    height: 434px;
    background: var(--card);
    box-shadow: 0 4px 14px rgba(0,0,0,0.12);
  }
  .card-frame { position: absolute; inset: 0; }

  /* Front */
  .front-info {
    position: absolute;
    left: 120px;
    top: 64px;
    color: var(--ink-grey);
  }
  .brand-name {
    font-family: "Dancing Script", cursive;
    font-weight: 700;
    font-size: 66px;
    color: var(--brand);
    line-height: 1.1;
    margin-bottom: 18px;
    margin-left: 30px;
  }
  .role {
    font-size: 13px;
    letter-spacing: 2.5px;
    text-transform: uppercase;
    margin-bottom: 8px;
  }
  .person {
    font-size: 30px;
    letter-spacing: 12px;
    color: var(--ink-dark);
    margin-bottom: 14px;
  }
  .phone {
    font-size: 25px;
    letter-spacing: 4px;
    margin-bottom: 10px;
  }
  .address {
    font-size: 20px;
    letter-spacing: 2.5px;
  }
  .woman-figure {
    position: absolute;
    right: 80px;
    bottom: 56px;
    width: 140px;
    height: 210px;
    border-radius: 70px 70px 20px 20px;
    background: linear-gradient(180deg, #f3d04a 0%, #8fd1c9 40%, #9db7ea 65%, #e79cc4 100%);
  }

  /* Back */
  .unicorn {
    position: absolute;
    left: 390px;
    top: 56px;
    width: 200px;
    height: 110px;
    border-radius: 55px 55px 35px 35px;
    background: linear-gradient(90deg, var(--silhouette) 0%, var(--silhouette) 55%, #f2a6c8 70%, #f3d04a 82%, #7cc7ea 100%);
  }
  .quote {
    position: absolute;
    left: 0;
    right: 0;
    top: 185px;
    text-align: center;
    font-family: "Dancing Script", cursive;
    font-weight: 700;
    font-size: 40px;
    line-height: 1.15;
  }
  .quote .w-yellow { color: var(--yellow); }
  .quote .w-orange { color: var(--orange); }
  .quote .w-pink { color: var(--pink); }
  .quote .w-purple { color: var(--purple); }
  .quote .w-blue { color: var(--blue); }
  .quote .w-green { color: var(--green); }
  .quote-source {
    position: absolute;
    left: 0;
    right: 0;
    top: 300px;
    text-align: center;
    font-size: 12px;
    letter-spacing: 4px;
    color: var(--ink-grey);
    text-transform: uppercase;
  }
</style>
</head>
<body>

  <section class="card card-front">
    <svg class="card-frame" width="760" height="434" viewBox="0 0 760 434" aria-hidden="true">
      <path d="M48 22 H712 A26 26 0 0 0 738 48 V386 A26 26 0 0 0 712 412 H48 A26 26 0 0 0 22 386 V48 A26 26 0 0 0 48 22 Z"
            fill="none" stroke="var(--frame)" stroke-width="4"/>
      <g fill="var(--frame)" font-size="16" font-family="sans-serif">
        <text x="18" y="33">★</text><text x="728" y="33">★</text>
        <text x="18" y="428">★</text><text x="728" y="428">★</text>
      </g>
    </svg>
    <div class="front-info">
      <h1 class="brand-name">Lark's Design</h1>
      <p class="role">Boutique Owner - Fashion Designer</p>
      <p class="person">MIRA</p>
      <p class="phone">021 587 3904</p>
      <p class="address">The Arbour - Christchurch</p>
    </div>
    <div class="woman-figure" role="img" aria-label="Silhouette of a woman in high heels wearing a rainbow-coloured dress with a scarf"></div>
  </section>

  <section class="card card-back">
    <svg class="card-frame" width="760" height="434" viewBox="0 0 760 434" aria-hidden="true">
      <path d="M48 22 H712 A26 26 0 0 0 738 48 V386 A26 26 0 0 0 712 412 H48 A26 26 0 0 0 22 386 V48 A26 26 0 0 0 48 22 Z"
            fill="none" stroke="var(--frame)" stroke-width="4"/>
      <g fill="var(--frame)" font-size="16" font-family="sans-serif">
        <text x="18" y="33">★</text><text x="728" y="33">★</text>
        <text x="18" y="428">★</text><text x="728" y="428">★</text>
      </g>
    </svg>
    <div class="unicorn" role="img" aria-label="White unicorn with a rainbow-coloured mane and tail"></div>
    <p class="quote">
      <span class="w-yellow">Sometimes</span> <span class="w-orange">the</span> <span class="w-orange">smallest</span> <span class="w-pink">things</span><br>
      <span class="w-pink">take</span> <span class="w-yellow">up</span> <span class="w-purple">the</span> <span class="w-purple">most</span> <span class="w-blue">room</span> <span class="w-blue">in</span> <span class="w-green">your</span> <span class="w-green">heart</span>
    </p>
    <p class="quote-source">Bramble the Mole</p>
  </section>

</body>
</html>
```